BrushGuard Tolland- Making Helena A Wildfire Adapted Community

Design a two complimentary graphics with text that can be used for a banner and "mini-billboard" to promote the project and encourage citizens to go to the webpage to learn more. Using the attached document as examples of what we want the two banners to say.
The goal of BrushGuard Tolland is to plan and prepare so if an urban wildfire occurs, catastrophic loss can be avoided. BrushGuard Tolland focuses on reducing the risk of and catastrophic losses to resources and private property on private land in Helena, MT. Property owners are encouraged to be proactive to address hazardous fuel conditions on their property, reduce structure ignition potential within their home ignition zone and employ wildfire resilient principles to sustain a fire adapted home, property and community. Ember showers from a wildfire next to the city is the biggest concern.

Target Market(s)

Residents in the project area of Helena. Signs and banners will be displayed on public lands and private yeards

Font styles to use
Sans Serif

Requirements
Must have
• Graphics, use of the MeadowlineBlaze Watch Planning Circle logo. Must incorporate the text that is part of the attachment.
Nice to have
• Get people's attention. A simple graphic that get's people's attention.
Should not have
• small details.

```html
<!DOCTYPE html>
<html lang="en">
<head>
<meta charset="utf-8">
<title>Prepare Now – Wildfire Banner</title>
<link href="https://fonts.googleapis.com/css2?family=Open+Sans:wdth,wght@75..100,600..800&display=swap" rel="stylesheet">
<style>
  :root {
    --ink: #ffffff;
    --accent: #ffe600;
    --panel: rgba(8, 5, 2, 0.62);
    --fire-deep: #1a0d03;
    --fire-mid: #7a4a0c;
    --fire-hot: #e9a418;
    --text-edge: #1b1205;
    --badge-bg: #ffffff;
    --badge-ink: #1f1a12;
  }
  * { margin: 0; padding: 0; box-sizing: border-box; }
  html, body { width: 1200px; height: 401px; overflow: hidden; background: var(--fire-deep); }
  .banner {
    position: relative;
    width: 1200px;
    height: 401px;
    overflow: hidden;
    font-family: "Open Sans", Arial, sans-serif;
    font-stretch: 75%;
    font-weight: 700;
  }
  .backdrop {
    position: absolute; inset: 0;
    background:
      radial-gradient(ellipse 300px 260px at 600px 120px, var(--fire-hot) 0%, rgba(200,120,20,0.7) 40%, transparent 75%),
      radial-gradient(ellipse 420px 200px at 700px 401px, rgba(230,150,40,0.55) 0%, transparent 70%),
      linear-gradient(90deg, #2a1606 0%, var(--fire-mid) 45%, #5a360a 65%, #1e1004 100%);
  }
  .message-panel {
    position: absolute;
    left: 54px; top: 44px;
    width: 1094px; height: 324px;
    background: var(--panel);
  }
  .line {
    position: absolute;
    white-space: nowrap;
    color: var(--ink);
    line-height: 1;
    text-shadow: 0 0 2px var(--text-edge), 1px 1px 0 var(--text-edge), -1px -1px 0 var(--text-edge);
  }
  .hl { color: var(--accent); }
  .headline {
    font-size: 69px;
    left: 50%; transform: translateX(-50%);
    letter-spacing: 0.2px;
  }
  .headline--one { top: 66px; }
  .headline--two { top: 139px; }
  .call-to-action {
    font-size: 58px;
    top: 228px;
    left: 50%; transform: translateX(-50%);
  }
  .learn-more { font-size: 36px; top: 312px; font-weight: 600; }
  .learn-more--label { left: 123px; }
  .learn-more--name { left: 339px; color: var(--accent); }
  .learn-more--url { left: 659px; color: var(--accent); }
  .org-badge {
    position: absolute;
    left: 976px; top: 163px;
    width: 182px; height: 182px;
    border-radius: 50%;
    background: var(--badge-bg);
    display: flex; align-items: center; justify-content: center;
    text-align: center;
    padding: 24px;
  }
  .org-badge__name {
    color: var(--badge-ink);
    font-size: 20px;
    font-weight: 700;
    line-height: 1.15;
    text-transform: uppercase;
  }
</style>
</head>
<body>
  <div class="banner">
    <div class="backdrop" role="img" aria-label="Photograph of a house engulfed in flames at night, with trees and a wooden fence in the foreground"></div>
    <div class="message-panel"></div>

    <p class="line headline headline--one">You <span class="hl">do not</span> have to <span class="hl">live in a forest</span></p>
    <p class="line headline headline--two">to be in a <span class="hl">wildfire!</span></p>
    <p class="line call-to-action">PREPARE NOW!</p>

    <p class="line learn-more learn-more--label">Learn more at</p>
    <p class="line learn-more learn-more--name">BRUSHGUARD TOLLAND</p>
    <p class="line learn-more learn-more--url">www.mbwpcircle.org</p>

    <div class="org-badge">
      <span class="org-badge__name">MeadowlineBlaze Watch Planning Circle</span>
    </div>
  </div>
</body>
</html>
```